Billboard for personal injury chiropractors office

We are a personal injury chiropractor clinic.
I need a Billboard with the company name as the dominating factor. Also a smaller picture or 2 of something creative, like a car accident or an arm in a cast off to the sides.
We Like something Clean and Simple and Eye Catching. Please make the picture Small and Off To The Side. The MAIN FOCUS areas are the… name Varden Chiropractic Clinic
At the top CAR ACCIDENT INJURY?
AND at the bottom our number 418-27-FLEXA.
Dr.Milo R. Varden in bold somewhere with the word chiropractor under the doctors name in a text.

Im open to red lettering on white backgrounds, red on yellow backgrounds and I'm also open to reds blues white and yellow. I'd prefer yellow if used be across the bottom.

I am uploading a very rough draft of what we are after along with a screenshot of the tv commercial showing the yellow

DO NOT USE THE LOGO ON THE COMMERCIAL. I JUST WANT THE NAME TYPED LIKE ON SAMPLE BILLBOARD.

Industry/Entity Type

Chiropractic

Colors
0054AA
0677BA
7BADD7
CADEEF
E8F1F8
FFF300
FFF600
FEFA6F
FFFEC7
FFFEE8
EB3D1F
EC4F4E
F09395
F8D3D4
FCEDEE

Requirements
Must have
• Eye catching ,bold

```html
<!DOCTYPE html>
<html lang="en">
<head>
<meta charset="utf-8">
<title>Varden Chiropractic Clinic – Billboard</title>
<link rel="stylesheet" href="https://fonts.googleapis.com/css2?family=Montserrat:wght@600;800;900&display=swap">
<style>
  :root {
    --stage: #e4e4e4;
    --red: #cc0000;
    --red-line: #e8b400;
    --yellow: #ffd500;
    --yellow-shadow: #c9a300;
    --ink: #0b0b0b;
    --white: #ffffff;
    --photo-dark: #1c1c1c;
    --photo-warm: #b89272;
  }
  html, body {
    margin: 0;
    width: 1000px;
    height: 1200px;
    overflow: hidden;
    background: var(--stage);
  }
  .stage {
    width: 1000px;
    height: 1200px;
    display: flex;
    align-items: center;
    justify-content: center;
  }
  .billboard {
    width: 920px;
    height: 269px;
    display: block;
    box-shadow: 0 14px 24px rgba(0,0,0,0.25);
  }
  .headline {
    font-family: "Montserrat", sans-serif;
    font-weight: 900;
    fill: var(--yellow);
    stroke: var(--red-line);
    stroke-width: 2;
    paint-order: stroke;
  }
  .clinic-name {
    font-family: "Montserrat", sans-serif;
    font-weight: 800;
    fill: var(--ink);
  }
  .doctor-name {
    font-family: "Montserrat", sans-serif;
    font-weight: 800;
    fill: var(--white);
  }
  .doctor-title {
    font-family: "Montserrat", sans-serif;
    font-weight: 600;
    fill: var(--white);
    letter-spacing: 5px;
  }
  .phone {
    font-family: "Montserrat", sans-serif;
    font-weight: 900;
    fill: var(--ink);
  }
  .text-shadow-grey { fill: #9a9a9a; }
  .text-shadow-gold { fill: var(--yellow-shadow); }
</style>
</head>
<body>
<main class="stage">
  <svg class="billboard" viewBox="0 0 1350 395" xmlns="http://www.w3.org/2000/svg">
    <defs>
      <linearGradient id="armPhotoTone" x1="0" y1="0" x2="1" y2="0">
        <stop offset="0" stop-color="var(--photo-warm)"/>
        <stop offset="0.25" stop-color="var(--photo-dark)"/>
        <stop offset="1" stop-color="#2a2a2a"/>
      </linearGradient>
      <radialGradient id="carPhotoTone" cx="0.55" cy="0.55" r="0.5">
        <stop offset="0" stop-color="#f2b400"/>
        <stop offset="0.6" stop-color="#f7d65c"/>
        <stop offset="1" stop-color="#ffffff"/>
      </radialGradient>
    </defs>

    <rect class="canvas-white" x="0" y="132" width="1350" height="263" fill="var(--white)"/>

    <g role="img" aria-label="Photo of a person with a bandaged arm in a cast and sling">
      <rect x="0" y="132" width="420" height="253" fill="url(#armPhotoTone)"/>
    </g>

    <g role="img" aria-label="Photo of a yellow sports car with a crashed front end">
      <rect x="1030" y="150" width="310" height="200" fill="url(#carPhotoTone)"/>
    </g>

    <rect class="top-band" x="0" y="0" width="1350" height="132" fill="var(--red)"/>
    <text class="headline" x="675" y="112" font-size="100" text-anchor="middle" textLength="1255" lengthAdjust="spacingAndGlyphs">CAR ACCIDENT INJURY?</text>

    <polygon class="clinic-band" points="270,132 1095,132 1040,217 325,217" fill="var(--yellow)"/>
    <text class="clinic-name text-shadow-grey" x="677" y="200" font-size="50" text-anchor="middle" textLength="700" lengthAdjust="spacingAndGlyphs">Varden Chiropractic Clinic</text>
    <text class="clinic-name" x="675" y="198" font-size="50" text-anchor="middle" textLength="700" lengthAdjust="spacingAndGlyphs">Varden Chiropractic Clinic</text>

    <polygon class="doctor-band" points="390,217 950,217 995,300 350,300" fill="var(--red)"/>
    <text class="doctor-name" x="675" y="261" font-size="38" text-anchor="middle" textLength="400" lengthAdjust="spacingAndGlyphs">Dr. Milo R. Varden</text>
    <text class="doctor-title" x="675" y="290" font-size="18" text-anchor="middle">CHIROPRACTOR</text>

    <polygon class="phone-band" points="255,300 1090,300 1135,385 210,385" fill="var(--yellow)"/>
    <rect class="bottom-strip" x="0" y="385" width="1350" height="10" fill="var(--yellow)"/>
    <text class="phone text-shadow-gold" x="679" y="375" font-size="68" text-anchor="middle" textLength="770" lengthAdjust="spacingAndGlyphs">CALL:  418-27-FLEXA</text>
    <text class="phone" x="675" y="371" font-size="68" text-anchor="middle" textLength="770" lengthAdjust="spacingAndGlyphs">CALL:  418-27-FLEXA</text>
  </svg>
</main>
</body>
</html>
```